VENTURE CAPITAL GROUP BUSINESS CARD DESIGN

Venture Capital Group based in SF looking for a bold business card design. No trendy colour explosion, 3D effects etc. Just "simple" optical effects. Works on your brain, keeps your eye focused and sticks to your mind.
Target Market(s)
Technology startups
Industry/Entity Type
Venture Capital
Contact Information for Business Card
BARNABY WHITLOCK
MANAGING PARTNER
817 FERN ST SAN FRANCISCO, CA 94111
415.555.0143 O
415.555.0167 F
415.555.0192 C
barn@halcyonridgefund.example

```html
<!DOCTYPE html>
<html lang="en">
<head>
<meta charset="utf-8">
<title>Halcyon Ridge Capital Group — Business Card</title>
<link href="https://fonts.googleapis.com/css2?family=Arimo:wght@400;700&family=Cinzel:wght@400;500&display=swap" rel="stylesheet">
<style>
  :root {
    --page: #e9e7e2;
    --card-white: #ffffff;
    --green-dark: #14632a;
    --green-mid: #1f8a3a;
    --green-light: #3aa64f;
    --grey-dark: #6d6e70;
    --grey-mid: #9a9b9d;
    --grey-light: #d4d5d6;
    --text-light: #ffffff;
    --text-soft: #e6f1e8;
    --text-muted: #c9cacb;
  }
  * { margin: 0; padding: 0; box-sizing: border-box; }
  html, body { width: 1200px; height: 950px; overflow: hidden; }
  body {
    background: var(--page);
    font-family: "Arimo", Arial, sans-serif;
    position: relative;
  }
  .card {
    position: absolute;
    left: 250px;
    width: 700px;
    height: 400px;
    border-radius: 6px;
    overflow: hidden;
    box-shadow: 0 10px 28px rgba(0,0,0,0.22);
  }
  .card--front { top: 40px; background: var(--card-white); }
  .card--back {
    top: 500px;
    background: linear-gradient(160deg, #8d8e90 0%, #7a7b7d 45%, #5f6062 100%);
  }
  .card__wave { position: absolute; inset: 0; width: 100%; height: 100%; }

  .brand {
    position: absolute;
    left: 40px;
    top: 46px;
    width: 300px;
    text-align: center;
    white-space: nowrap;
  }
  .brand__dot {
    width: 86px; height: 86px;
    margin: 0 auto 12px;
    border-radius: 50%;
    background: radial-gradient(circle at 40% 35%, #ffffff 0%, #e3e4e5 60%, #c7c8ca 100%);
  }
  .brand__name {
    font-family: "Cinzel", Georgia, serif;
    font-weight: 500;
    font-size: 30px;
    letter-spacing: 0.5px;
    color: var(--green-mid);
    line-height: 1;
  }
  .brand__sub {
    margin-top: 6px;
    font-family: "Cinzel", Georgia, serif;
    font-weight: 500;
    font-size: 11px;
    letter-spacing: 3px;
    color: var(--green-mid);
  }

  .contact {
    position: absolute;
    right: 36px;
    top: 206px;
    text-align: right;
    color: var(--text-light);
    white-space: nowrap;
  }
  .contact__name { font-weight: 700; font-size: 24px; line-height: 28px; }
  .contact__title { font-size: 18px; line-height: 22px; color: var(--text-soft); margin-bottom: 8px; }
  .contact__line {
    display: flex;
    justify-content: flex-end;
    align-items: center;
    gap: 8px;
    font-size: 17px;
    line-height: 25px;
  }
  .contact__icon { width: 16px; height: 16px; fill: var(--text-light); flex: none; }
  .contact__line--plain { padding-right: 24px; }

  .back-brand {
    position: absolute;
    left: 0; right: 0;
    top: 82px;
    text-align: center;
  }
  .back-brand__dot {
    width: 150px; height: 150px;
    margin: 0 auto 18px;
    border-radius: 50%;
    background: radial-gradient(circle at 40% 35%, #ffffff 0%, #e1e2e3 60%, #bdbec0 100%);
  }
  .back-brand__name {
    font-family: "Cinzel", Georgia, serif;
    font-weight: 500;
    font-size: 30px;
    line-height: 1;
    color: var(--text-light);
    letter-spacing: 0.5px;
  }
  .back-url {
    position: absolute;
    right: 150px;
    bottom: 66px;
    font-size: 18px;
    letter-spacing: 1px;
    color: var(--text-muted);
  }
</style>
</head>
<body>

<section class="card card--front" aria-label="Business card front">
  <svg class="card__wave" viewBox="0 0 700 400" preserveAspectRatio="none" aria-hidden="true">
    <defs>
      <linearGradient id="greenFill" x1="0" y1="0" x2="1" y2="1">
        <stop offset="0" stop-color="#1a7a33"/>
        <stop offset="0.35" stop-color="#2f9a45"/>
        <stop offset="1" stop-color="#135a27"/>
      </linearGradient>
      <linearGradient id="greyBand" x1="0" y1="0" x2="1" y2="0">
        <stop offset="0" stop-color="#d8d9da"/>
        <stop offset="0.5" stop-color="#8f9092"/>
        <stop offset="1" stop-color="#c5c6c7"/>
      </linearGradient>
    </defs>
    <path d="M0 222 C 120 268, 240 292, 360 226 C 420 190, 510 126, 700 121 L700 400 L0 400 Z" fill="url(#greyBand)"/>
    <path d="M0 238 C 120 292, 250 318, 368 240 C 425 200, 515 138, 700 134 L700 400 L0 400 Z" fill="#ffffff"/>
    <path d="M0 246 C 120 304, 250 330, 372 252 C 430 210, 520 150, 700 145 L700 400 L0 400 Z" fill="url(#greenFill)"/>
  </svg>

  <div class="brand">
    <div class="brand__dot"></div>
    <div class="brand__name">Halcyon Ridge</div>
    <div class="brand__sub">CAPITAL GROUP</div>
  </div>

  <div class="contact">
    <div class="contact__name">Barnaby Whitlock</div>
    <div class="contact__title">Managing Partner</div>
    <div class="contact__line">415.555.0143
      <svg class="contact__icon" viewBox="0 0 16 16" aria-label="Office"><path d="M2 6c0-2 3-3 6-3s6 1 6 3l-2 1-1-2H5L4 7z"/><rect x="3" y="8" width="10" height="6" rx="1"/></svg>
    </div>
    <div class="contact__line">415.555.0192
      <svg class="contact__icon" viewBox="0 0 16 16" aria-label="Mobile"><rect x="4" y="1" width="8" height="14" rx="1.5"/><rect x="5.5" y="3" width="5" height="8" fill="#1f8a3a"/></svg>
    </div>
    <div class="contact__line">415.555.0167
      <svg class="contact__icon" viewBox="0 0 16 16" aria-label="Fax"><rect x="4" y="1" width="8" height="5"/><rect x="1" y="6" width="14" height="7" rx="1"/><rect x="4" y="11" width="8" height="4" fill="#1f8a3a"/></svg>
    </div>
    <div class="contact__line">barn@halcyonridgefund.example
      <svg class="contact__icon" viewBox="0 0 16 16" aria-label="Email"><rect x="1" y="3" width="14" height="10" rx="1"/><path d="M1.5 3.5 8 9l6.5-5.5" fill="none" stroke="#1f8a3a" stroke-width="1.3"/></svg>
    </div>
    <div class="contact__line contact__line--plain">817 Fern ST San Francisco, CA 94111</div>
  </div>
</section>

<section class="card card--back" aria-label="Business card back">
  <div class="back-brand">
    <div class="back-brand__dot"></div>
    <div class="back-brand__name">Halcyon Ridge</div>
  </div>
  <div class="back-url">halcyonridgefund.example</div>
</section>

</body>
</html>
```